Private Investment Firm Needs PowerPoint Presentation Template

Design PowerPoint template, take Ridgefell-submitted rough presentation draft, and drop it into new template. See attached Project Brief file for more detail.
Updates

Some decent designs have been submitted but they seem to lack the understanding of our target markets. I am hopeful that more time and feedback will result in better results.

Target Market(s)

Private company owners and intermediaries.

Font styles to use
Serif

Colors
3176b5

Requirements
Must have
• See attached Project Brief.
Nice to have
Should not have
• No B2C fluff--this is a B2B project.

```html
<!DOCTYPE html>
<html lang="en">
<head>
<meta charset="UTF-8">
<title>What Is Non-Control Capital? – Ridgefell Capital</title>
<link href="https://fonts.googleapis.com/css2?family=Figtree:wght@400;500&family=Montserrat:wght@700&family=Playfair+Display:wght@400&display=swap" rel="stylesheet">
<style>
  :root {
    --brand-blue: #0170c1;
    --icon-tone: rgba(255, 255, 255, 0.2);
    --ink: #1d1d1f;
    --paper: #ffffff;
  }
  html, body {
    margin: 0;
    padding: 0;
    width: 1200px;
    height: 676px;
    overflow: hidden;
    background: var(--paper);
  }
  .slide {
    position: relative;
    width: 1200px;
    height: 676px;
    background: var(--paper);
    font-family: "Figtree", "Helvetica Neue", Arial, sans-serif;
    color: var(--ink);
  }
  .side-rail {
    position: absolute;
    left: 0; top: 0;
    width: 44px; height: 676px;
    background: var(--brand-blue);
  }
  .side-rail__url {
    position: absolute;
    left: 22px; top: 336px;
    transform: translate(-50%, -50%) rotate(-90deg);
    white-space: nowrap;
    font-family: "Playfair Display", Georgia, serif;
    font-size: 14px;
    letter-spacing: 0.3px;
    color: var(--paper);
  }
  .edge-rail {
    position: absolute;
    right: 0; top: 0;
    width: 11px; height: 676px;
    background: var(--brand-blue);
  }
  .page-number {
    position: absolute;
    right: 40px; top: 16px;
    font-family: "Playfair Display", Georgia, serif;
    font-size: 20px;
    color: var(--ink);
  }
  .slide-title {
    position: absolute;
    left: 86px; top: 78px;
    margin: 0;
    font-family: "Montserrat", Arial, sans-serif;
    font-weight: 700;
    font-size: 29px;
    letter-spacing: 0.2px;
    color: var(--brand-blue);
  }
  .lead {
    position: absolute;
    left: 86px; top: 144px;
    margin: 0;
    padding-left: 28px;
    white-space: nowrap;
    font-size: 17.4px;
    line-height: 28px;
    letter-spacing: 0.45px;
  }
  .lead::before {
    content: "";
    position: absolute;
    left: 0; top: 8px;
    width: 12px; height: 12px;
    background: var(--brand-blue);
  }
  .retained-panel {
    position: absolute;
    left: 280px; top: 254px;
    width: 909px; height: 360px;
    background: var(--brand-blue);
    color: var(--paper);
  }
  .control-item__icon {
    position: absolute;
    width: 72px; height: 72px;
    border-radius: 8px;
    background: var(--icon-tone);
    transform: translateX(-50%);
  }
  .control-item__label {
    position: absolute;
    width: 320px;
    margin: 0;
    transform: translateX(-50%);
    text-align: center;
    font-size: 14.6px;
    line-height: 22px;
    letter-spacing: 0.3px;
  }
  .icon--economics { left: 216px; top: 52px; }
  .icon--operations { left: 590px; top: 52px; }
  .icon--strategy { left: 220px; top: 180px; }
  .icon--board { left: 592px; top: 196px; height: 56px; }
  .label--economics { left: 211px; top: 141px; }
  .label--operations { left: 585px; top: 141px; }
  .label--strategy { left: 220px; top: 270px; }
  .label--board { left: 586px; top: 270px; }
  .brand {
    position: absolute;
    left: 66px; top: 614px;
    display: flex;
    align-items: center;
    gap: 10px;
  }
  .brand__mark {
    width: 36px; height: 36px;
    border-radius: 50%;
    background: var(--brand-blue);
  }
  .brand__name {
    font-size: 17px;
    font-weight: 500;
    letter-spacing: 1.5px;
    color: var(--brand-blue);
  }
</style>
</head>
<body>
<main class="slide">
  <div class="side-rail"><span class="side-rail__url">www.ridgefellcapital.com</span></div>
  <div class="edge-rail"></div>
  <span class="page-number">2</span>

  <h1 class="slide-title">WHAT IS NON-CONTROL CAPITAL?</h1>
  <p class="lead">Non-Control Capital is an investment which is primarily used for the on-<br>going operation and/or growth of a business but also allows the current<br>owners to retain:</p>

  <section class="retained-panel">
    <div class="control-item__icon icon--economics" role="img" aria-label="Line icon for business economics"></div>
    <p class="control-item__label label--economics">Control of the Business Economics</p>

    <div class="control-item__icon icon--operations" role="img" aria-label="Line icon for business operations"></div>
    <p class="control-item__label label--operations">Control of the Business Operations</p>

    <div class="control-item__icon icon--strategy" role="img" aria-label="Line icon for strategy and decision making"></div>
    <p class="control-item__label label--strategy">Control of Strategy and<br>Key Decision Making</p>

    <div class="control-item__icon icon--board" role="img" aria-label="Line icon for the board of directors"></div>
    <p class="control-item__label label--board">Control of the Board of Directors</p>
  </section>

  <div class="brand">
    <span class="brand__mark" aria-hidden="true"></span>
    <span class="brand__name">RIDGEFELL CAPITAL</span>
  </div>
</main>
</body>
</html>
```